Rw construct holdings pty ltd

This is a development and construction company. Website can be set up on our domain rwbuildgroup.net if we could change the domain to rwbuildgroup.com.au would be great

Want the page to have eye catching designs, red, black and white are the preffered colours.

Check out www.tolumine.com.au it is my former company with my partner which i am now venturing out on my own, that is the perfect example of the website i want even allot of the information would be the same

Industry/Entity Type

Construction

Coding

Coded - Design and coding required

Number of Pages Required

5+ page

Requirements
Must have
• Company logo eye catching designs

```html
<!DOCTYPE html>
<html lang="en">
<head>
<meta charset="utf-8">
<title>RW Build Group</title>
<link href="https://fonts.googleapis.com/css2?family=Questrial&display=swap" rel="stylesheet">
<style>
:root{
  --red:#e8401f;
  --red-soft:#ee5533;
  --black:#0c0c0c;
  --ink:#1a1a1a;
  --slate:#3e434c;
  --card-grey:#6c717b;
  --light:#f3f3f3;
  --white:#ffffff;
  --text:#333;
}
*{box-sizing:border-box;margin:0;padding:0}
html,body{width:1200px;height:3394px;overflow:hidden}
body{position:relative;background:var(--white);font-family:"Questrial",sans-serif;color:var(--ink)}
.abs{position:absolute}
.brand{font-size:20px;letter-spacing:1px;color:var(--ink);font-weight:400;display:flex;align-items:center;gap:8px}
.brand .dot{width:10px;height:10px;background:var(--red);border-radius:50%}
.nav a{position:absolute;top:30px;font-size:11px;letter-spacing:.5px;color:var(--ink);text-decoration:none}
.btn{position:absolute;border-radius:16px;font-size:11px;letter-spacing:.5px;display:flex;align-items:center;justify-content:center;text-transform:uppercase}
.btn-outline-red{border:2px solid var(--red);color:var(--red);background:transparent}
.btn-red{background:var(--red);color:var(--white)}
.btn-white{background:var(--white);color:var(--red)}
.btn-ghost{border:2px solid var(--white);color:var(--white)}
.eyebrow{font-size:18px;letter-spacing:.5px;color:var(--ink);text-transform:uppercase}
.heading{font-size:30px;letter-spacing:.8px;color:var(--red);text-transform:uppercase;line-height:1.17}
.photo{position:absolute}
.circle-arrow{position:absolute;width:30px;height:30px;border-radius:50%;display:flex;align-items:center;justify-content:center}
.body-text{font-size:9.5px;line-height:1.6;color:var(--text)}
.service-card{position:absolute;top:1314px;width:249px;height:180px;border:1px solid rgba(255,255,255,.7);padding:20px 18px;color:var(--white)}
.service-card h3{font-size:12px;font-weight:400;margin-top:12px;letter-spacing:.3px}
.service-card p{font-size:10px;line-height:1.5;margin-top:14px}
.field{position:absolute;background:var(--white);font-size:9.5px;color:#555;padding:10px 12px}
.footer h4{font-size:12px;color:var(--red);font-weight:400;letter-spacing:.5px}
.footer li{list-style:none;font-size:9px;color:var(--white);line-height:19px}
.social{position:absolute;left:969px;width:30px;height:30px;border-radius:50%;background:#3a3a3a}
</style>
</head>
<body>

<!-- Header -->
<header class="site-header">
  <div class="abs brand" style="left:200px;top:26px">RW BUILD GROUP<span class="dot"></span></div>
  <nav class="nav">
    <a style="left:466px;color:var(--red)">HOME</a>
    <a style="left:523px">ABOUT US</a>
    <a style="left:601px">SERVICES</a>
    <a style="left:678px">PROJECTS</a>
    <a style="left:765px;color:var(--red)">
      <svg width="11" height="11" viewBox="0 0 24 24" style="vertical-align:-1px;margin-right:4px"><path d="M6.6 10.8a15 15 0 006.6 6.6l2.2-2.2a1 1 0 011-.25 11.4 11.4 0 003.6.6 1 1 0 011 1V20a1 1 0 01-1 1A17 17 0 013 4a1 1 0 011-1h3.5a1 1 0 011 1 11.4 11.4 0 00.6 3.6 1 1 0 01-.25 1z" fill="none" stroke="#e8401f" stroke-width="2"/></svg>555-010-2040</a>
  </nav>
  <div class="btn btn-outline-red" style="left:887px;top:22px;width:113px;height:31px">Contact Us</div>
</header>

<!-- Hero -->
<section class="hero">
  <div class="photo" role="img" aria-label="Bright open-plan living room with fireplace and dining area" style="left:0;top:75px;width:1200px;height:468px;background:linear-gradient(120deg,#9a9a98 0%,#b8b6b2 40%,#8f8d89 70%,#a29d95 100%)"></div>
  <div class="abs" style="left:0;top:75px;width:1200px;height:468px;background:rgba(40,40,40,.25)"></div>
  <div class="abs" style="left:0;top:222px;width:1200px;text-align:center;color:var(--white);font-size:34px;letter-spacing:3px">RW BUILD</div>
  <h1 class="abs" style="left:0;top:305px;width:1200px;text-align:center;color:var(--white);font-size:42px;font-weight:400;letter-spacing:1px">SPACIOUS WALK-IN ROBES</h1>
  <div class="btn btn-ghost" style="left:537px;top:375px;width:126px;height:30px;font-size:10px">View Projects</div>
  <div class="circle-arrow" style="left:94px;top:294px;background:rgba(255,255,255,.35)"><svg width="10" height="10" viewBox="0 0 10 10"><path d="M6.5 1.5L3 5l3.5 3.5" stroke="#fff" stroke-width="1.3" fill="none"/></svg></div>
  <div class="circle-arrow" style="left:1075px;top:294px;background:rgba(255,255,255,.35)"><svg width="10" height="10" viewBox="0 0 10 10"><path d="M3.5 1.5L7 5 3.5 8.5" stroke="#fff" stroke-width="1.3" fill="none"/></svg></div>
  <svg class="abs" style="left:571px;top:500px" width="60" height="12">
    <circle cx="6" cy="6" r="4.5" fill="none" stroke="#fff"/><circle cx="21" cy="6" r="4.5" fill="none" stroke="#fff"/><circle cx="21" cy="6" r="2" fill="#fff"/><circle cx="36" cy="6" r="4.5" fill="none" stroke="#fff"/><circle cx="51" cy="6" r="4.5" fill="none" stroke="#fff"/>
  </svg>
</section>

<!-- About -->
<section class="about">
  <div class="abs eyebrow" style="left:200px;top:641px">Innovation &amp; Quality For</div>
  <h2 class="abs heading" style="left:200px;top:666px;width:360px;font-weight:400">Building Your Dream Home</h2>
  <div class="abs body-text" style="left:200px;top:750px;width:345px">
    <p>We at Tolumine believe that building your dream home shouldn't cost your life savings! Nor should it take a lifetime to build!</p>
    <p style="font-size:10.5px;color:var(--ink);margin:12px 0">We are determined to make your new build your forever home!</p>
    <p>At Tolumine we have one goal: to create innovative designs and build quality homes, to suit all budgets. A simple but powerful philosophy that typifies the way we do business. We believe that the quality of our service can assist our clients to reduce their costs by getting it right the first time.</p>
    <p style="margin-top:14px">We started with the burning desire to build homes where people would truly love to live. That's what we wanted to achieve above all else and that's what we're still focused on ...</p>
  </div>
  <div class="btn btn-outline-red" style="left:200px;top:974px;width:113px;height:30px">About Us</div>
  <div class="abs" style="left:731px;top:607px;width:268px;height:436px;border:1.5px solid var(--red)"></div>
  <div class="photo" role="img" aria-label="Living room with tall windows and garden view" style="left:743px;top:619px;width:244px;height:374px;background:linear-gradient(180deg,#e7e8e6 0%,#b7c2a8 45%,#a89b8a 75%,#d7d3cc 100%)"></div>
  <div class="photo" role="img" aria-label="Lounge with chandelier and dark sofa" style="left:612px;top:787px;width:177px;height:243px;background:linear-gradient(180deg,#ece9e4 0%,#c9c2b8 55%,#5a5550 100%);border-right:4px solid #fff"></div>
</section>

<!-- Services -->
<section class="services">
  <div class="photo" role="img" aria-label="Interior shelving tinted red" style="left:612px;top:1106px;width:588px;height:456px;background:linear-gradient(135deg,#e8401f 0%,#e2502f 60%,#ea5a3a 100%)"></div>
  <div class="photo" role="img" aria-label="Dark living room with sofa" style="left:0;top:1168px;width:794px;height:456px;background:linear-gradient(135deg,#1c1c1c 0%,#111 60%,#181818 100%)"></div>
  <div class="abs eyebrow" style="left:200px;top:1228px;color:var(--white)">What We Do</div>
  <h2 class="abs heading" style="left:200px;top:1252px;font-weight:400">Services We Provide</h2>

  <div class="service-card" style="left:200px">
    <svg width="36" height="40" viewBox="0 0 36 40" fill="none" stroke="#fff" stroke-width="1.4"><circle cx="18" cy="15" r="11"/><circle cx="18" cy="15" r="6"/><path d="M11 24l-4 12 6-3 3 5 2-10M25 24l4 12-6-3-3 5-2-10"/></svg>
    <h3>EXCEPTIONAL CLIENT SERVICE</h3>
    <p>We create a culture of warmth and belonging, where everyone is welcome!</p>
  </div>
  <div class="service-card" style="left:475px;background:var(--card-grey);border-color:var(--card-grey)">
    <svg width="36" height="40" viewBox="0 0 36 40" fill="none" stroke="#fff" stroke-width="1.4"><rect x="4" y="5" width="28" height="33" rx="2"/><rect x="12" y="2" width="12" height="6"/><path d="M10 16h16M10 22h16M10 28h16"/></svg>
    <h3>ACCOUNTABILITY</h3>
    <p>Delivering our very best in all we do and holding ourselves accountable for results.</p>
  </div>
  <div class="service-card" style="left:750px">
    <svg width="52" height="40" viewBox="0 0 52 40" fill="none" stroke="#fff" stroke-width="1.4"><circle cx="26" cy="10" r="6"/><circle cx="11" cy="18" r="5"/><circle cx="41" cy="18" r="5"/><path d="M16 36c0-8 4-14 10-14s10 6 10 14M3 38c0-6 3-10 8-10M49 38c0-6-3-10-8-10"/></svg>
    <h3>LEADERSHIP</h3>
    <p>Acting with courage, challenging the status quo and finding new ways to grow our company and each other.</p>
  </div>

  <div class="circle-arrow" style="left:494px;top:1527px;border:1.5px solid var(--red)"><svg width="10" height="10" viewBox="0 0 10 10"><path d="M6.5 1.5L3 5l3.5 3.5" stroke="#e8401f" stroke-width="1.3" fill="none"/></svg></div>
  <div class="btn btn-outline-red" style="left:543px;top:1527px;width:113px;height:30px;font-size:10px">View All</div>
  <div class="circle-arrow" style="left:675px;top:1527px;border:1.5px solid var(--red)"><svg width="10" height="10" viewBox="0 0 10 10"><path d="M3.5 1.5L7 5 3.5 8.5" stroke="#e8401f" stroke-width="1.3" fill="none"/></svg></div>
</section>

<!-- Projects -->
<section class="projects">
  <div class="abs eyebrow" style="left:0;width:1200px;text-align:center;top:1683px">Completed Projects</div>
  <h2 class="abs heading" style="left:0;width:1200px;text-align:center;top:1708px;font-weight:400">See Our Latest Work</h2>
  <div class="photo" role="img" aria-label="Kitchen with timber dining table" style="left:200px;top:1768px;width:387px;height:157px;background:linear-gradient(180deg,#d9d7d3 0%,#eeeae4 50%,#a7856a 100%)"></div>
  <div class="photo" role="img" aria-label="Modern house exterior at dusk" style="left:200px;top:1949px;width:181px;height:156px;background:linear-gradient(180deg,#6f7880 0%,#3a3a38 55%,#3e5a2e 100%)"></div>
  <div class="photo" role="img" aria-label="Dining room shown under red hover tint" style="left:406px;top:1949px;width:181px;height:156px;background:linear-gradient(135deg,#ea5a3a,#e8401f)"></div>
  <div class="abs" style="left:418px;top:1961px;width:157px;height:132px;border:1px solid rgba(255,255,255,.7)"></div>
  <svg class="abs" style="left:487px;top:2017px" width="20" height="20"><path d="M10 0v20M0 10h20" stroke="#fff" stroke-width="1.2"/></svg>
  <div class="photo" role="img" aria-label="Living room with black armchairs and glass doors" style="left:612px;top:1768px;width:387px;height:337px;background:linear-gradient(180deg,#8c8f8e 0%,#c9c7c2 45%,#7a7671 75%,#9a948b 100%)"></div>
  <div class="btn btn-red" style="left:543px;top:2137px;width:113px;height:29px;font-size:10px">View All</div>
</section>

<!-- Testimonials -->
<section class="testimonials">
  <div class="abs" style="left:587px;top:2231px;width:613px;height:444px;background:var(--light)"></div>
  <div class="photo" role="img" aria-label="Living room with blue sofa and view to garden" style="left:0;top:2231px;width:587px;height:444px;background:linear-gradient(180deg,#f2f1ef 0%,#d9dcd7 30%,#6c7a5c 55%,#8a6a52 75%,#b4bcc8 100%)"></div>
  <div class="abs eyebrow" style="left:612px;top:2265px">Testimonials</div>
  <h2 class="abs heading" style="left:612px;top:2289px;font-weight:400">What Our Clients Say</h2>
  <div class="abs" style="left:475px;top:2351px;width:524px;height:224px;background:var(--slate);padding:22px 26px;color:var(--white)">
    <p style="font-style:italic;font-size:11.5px;line-height:1.75">"I have recommended Tolumine Construction &amp; Development Pty Ltd to many of my friends who have viewed the work they have done for us. I would not hesitate to recommend them in the future. We are very pleased with the work and especially the state the site was left in on completion."</p>
    <div style="display:flex;align-items:center;margin-top:20px;gap:14px">
      <div style="width:48px;height:48px;border-radius:50%;background:var(--red);display:flex;align-items:center;justify-content:center;font-size:22px;letter-spacing:2px">66</div>
      <div><div style="font-size:13px">Marek Dalloway</div><div style="font-size:9.5px;margin-top:2px">Westbrook</div></div>
    </div>
  </div>
  <div class="circle-arrow" style="left:613px;top:2610px;border:1.5px solid var(--red)"><svg width="10" height="10" viewBox="0 0 10 10"><path d="M6.5 1.5L3 5l3.5 3.5" stroke="#e8401f" stroke-width="1.3" fill="none"/></svg></div>
  <div class="circle-arrow" style="left:651px;top:2610px;background:var(--red)"><svg width="10" height="10" viewBox="0 0 10 10"><path d="M3.5 1.5L7 5 3.5 8.5" stroke="#fff" stroke-width="1.3" fill="none"/></svg></div>
</section>

<!-- Partner & Contact -->
<section class="partner">
  <div class="abs" style="left:0;top:2675px;width:1200px;height:313px;background:var(--red)"></div>
  <div class="abs" style="left:0;top:2988px;width:1200px;height:406px;background:var(--black)"></div>
  <h2 class="abs" style="left:198px;top:2717px;color:var(--white);font-size:38px;font-weight:400;letter-spacing:1px">PARTNER WITH US</h2>
  <div class="abs" style="left:198px;top:2760px;color:var(--white);font-size:20px;letter-spacing:.5px">FOR ALL YOUR BUILDING AND CONSTRUCTION NEEDS.</div>
  <div class="btn btn-white" style="left:887px;top:2735px;width:113px;height:30px">Contact Us</div>

  <div class="abs" style="left:200px;top:2827px;width:799px;height:274px;background:var(--slate)"></div>
  <div class="abs eyebrow" style="left:0;width:1200px;text-align:center;top:2856px;color:var(--white)">Say Hello!</div>
  <h2 class="abs heading" style="left:0;width:1200px;text-align:center;top:2880px;font-weight:400">Build Your Dream Home</h2>
  <div class="field" style="left:294px;top:2935px;width:199px;height:30px">Name</div>
  <div class="field" style="left:500px;top:2935px;width:199px;height:30px">Email</div>
  <div class="field" style="left:707px;top:2935px;width:199px;height:30px">Phone</div>
  <div class="field" style="left:294px;top:2972px;width:612px;height:55px">Message...</div>
  <div class="btn btn-red" style="left:543px;top:3044px;width:113px;height:29px;font-size:10px">Submit</div>
</section>

<!-- Footer -->
<footer class="footer">
  <div class="abs brand" style="left:200px;top:3208px;color:var(--white);font-size:22px">RW BUILD GROUP<span class="dot"></span></div>
  <h4 class="abs" style="left:475px;top:3168px">CONTACT US</h4>
  <svg class="abs" style="left:475px;top:3201px" width="18" height="18" viewBox="0 0 24 24"><path d="M6.6 10.8a15 15 0 006.6 6.6l2.2-2.2a1 1 0 011-.25 11.4 11.4 0 003.6.6 1 1 0 011 1V20a1 1 0 01-1 1A17 17 0 013 4a1 1 0 011-1h3.5a1 1 0 011 1 11.4 11.4 0 00.6 3.6 1 1 0 01-.25 1z" fill="none" stroke="#e8401f" stroke-width="1.6"/></svg>
  <div class="abs" style="left:503px;top:3198px;font-size:9px;color:var(--red)">Call</div>
  <div class="abs" style="left:503px;top:3213px;font-size:11px;color:var(--white)">(555)-010-2040</div>
  <svg class="abs" style="left:475px;top:3243px" width="18" height="16" viewBox="0 0 18 16"><rect x="1" y="3" width="16" height="11" fill="none" stroke="#e8401f" stroke-width="1.3"/><path d="M1 3l8 6 8-6" fill="none" stroke="#e8401f" stroke-width="1.3"/></svg>
  <div class="abs" style="left:503px;top:3240px;font-size:9px;color:var(--red)">Email</div>
  <div class="abs" style="left:503px;top:3255px;font-size:11px;color:var(--white)">info@rwbuildgroup.com.au</div>
  <h4 class="abs" style="left:749px;top:3168px">QUICK LINKS</h4>
  <ul class="abs" style="left:749px;top:3194px">
    <li>Home</li><li>About Us</li><li>Services</li><li>Projects</li><li>Contact Us</li>
  </ul>
  <div class="social" role="img" aria-label="Social profile link" style="top:3168px"></div>
  <div class="social" role="img" aria-label="Social profile link" style="top:3206px;background:var(--red)"></div>
  <div class="social" role="img" aria-label="Social profile link" style="top:3244px"></div>
  <div class="abs" style="left:200px;top:3330px;font-size:9px;color:var(--white)">© 2021 <span style="color:var(--red)">RW BUILD GROUP</span>. ALL RIGHTS RESERVED</div>
</footer>

</body>
</html>
```